Design a peer-to-peer car rental marketplace website

Hello, would need in the next 24h the designs of the 4 following pages of a peer-to-peer car rental website called Wheelora (a website concept similar to [login to view URL]) :

- Homepage
- Results page
- Car details page
- Checkout

Find attached to the description THE BRIEF TO DOWNLOAD, the ideal fonts to use for the designs and the logo.

The winner will be hired again if he accepts, to design the rest of the pages for another project.

The conversion to HTML won’t be required but I will need the source files .ai, .psd or pdf after the contest.

I will be very active in the rating process, do not wait to finish all pages before submitting something. If you’re done with the homepage, submit it and we will work together.

Thanking in advance every freelancer for their time.

```html
<!DOCTYPE html>
<html lang="en">
<head>
<meta charset="utf-8">
<title>Wheelora – Peer-to-peer car rental</title>
<link rel="stylesheet" href="https://fonts.googleapis.com/css2?family=Roboto:wght@300;400;500;700&family=Open+Sans:wght@300;400;600&display=swap">
<style>
:root{
  --accent:#e0542a;
  --ink:#3c3c3c;
  --muted:#6b6b6b;
  --soft:#f6f6f6;
  --line:#e4e4e4;
  --white:#ffffff;
  --footer:#252525;
}
*{box-sizing:border-box;margin:0;padding:0}
html,body{width:1200px;height:3345px;overflow:hidden}
body{position:relative;font-family:"Roboto",Arial,sans-serif;color:var(--ink);background:var(--white)}
.abs{position:absolute}
.center{left:0;width:1200px;text-align:center}

/* hero */
.hero{left:0;top:0;width:1200px;height:557px;background:linear-gradient(180deg,#8e959c 0%,#6d7276 35%,#3f4244 65%,#6a6763 100%)}
.hero-car{left:140px;top:120px;width:920px;height:420px;border-radius:200px 260px 60px 60px;background:radial-gradient(ellipse at 50% 55%,#2a2c2e 0%,#3a3c3f 55%,rgba(60,62,64,0) 75%)}
.brand{left:207px;top:28px;font:700 26px "Roboto",sans-serif;color:var(--accent)}
.nav{top:32px;left:473px;width:391px;height:30px;border-bottom:1px solid rgba(255,255,255,.55)}
.nav a{position:absolute;top:0;font:400 12px "Roboto",sans-serif;color:var(--white);text-decoration:none}
.pill{top:31px;height:17px;border-radius:9px;font:400 9px "Roboto",sans-serif;line-height:17px;text-align:center}
.pill.login{left:981px;width:44px;background:var(--white);color:var(--muted)}
.pill.rent{left:1041px;width:68px;background:var(--accent);color:var(--white)}
.hero-title{top:190px;font:300 35px/47px "Open Sans",sans-serif;color:var(--white)}
.hero-sub{top:307px;font:400 12px "Open Sans",sans-serif;color:var(--white)}
.search{left:315px;top:404px;width:569px;height:56px;background:var(--white);display:flex;align-items:center}
.search .field{position:relative;height:38px;padding:12px 0 0 28px;border-right:1px solid var(--line)}
.search .label{font:500 7px "Roboto",sans-serif;color:var(--ink)}
.search .value{font:400 8px "Roboto",sans-serif;color:#b5b5b5;margin-top:4px}
.search .chev{position:absolute;right:14px;top:20px}
.search .go{display:flex;align-items:center;gap:10px;padding-left:18px;font:400 13px "Roboto",sans-serif;color:#9a9a9a}
.hero-dots{top:522px;left:570px;display:flex;gap:13px}
.hero-dots span{width:10px;height:10px;border-radius:50%;background:rgba(255,255,255,.6)}
.hero-dots span.on{background:var(--white)}

/* shared */
.section-title{font:400 24px "Roboto",sans-serif;color:var(--ink)}
.rule{width:88px;height:1px;background:var(--accent);left:556px}
.body-text{font:400 12px/15px "Roboto",sans-serif;color:var(--muted)}

/* features */
.intro{left:316px;top:714px;width:568px;text-align:center}
.feature{top:878px;width:210px;text-align:center}
.feature svg{display:block;margin:0 auto}
.feature h3{margin-top:44px;font:400 18px "Roboto",sans-serif;color:var(--ink)}
.feature p{margin-top:20px;font:400 11.5px/15px "Roboto",sans-serif;color:var(--muted)}

/* featured cars */
.featured{left:0;top:1176px;width:1200px;height:524px;background:var(--soft)}
.card{top:1351px;width:351px;height:216px;background:var(--white);box-shadow:0 1px 4px rgba(0,0,0,.12);display:flex}
.card .photo{width:167px;height:216px;flex:none}
.card .info{position:relative;padding:21px 0 0 19px;width:184px}
.card h4{font:400 13px "Roboto",sans-serif;color:var(--ink)}
.card .desc{margin-top:18px;font:400 9.5px/12px "Roboto",sans-serif;color:var(--muted);width:150px}
.card .price{margin-top:10px;font:400 12.5px "Roboto",sans-serif;color:var(--ink)}
.card .stars{margin-top:12px;display:flex;align-items:center;gap:3px;font:400 9px "Roboto",sans-serif;color:#999}
.card .divider{margin-top:5px;width:158px;height:1px;background:var(--line)}
.card .loc{margin-top:6px;display:flex;align-items:center;gap:6px;font:400 9px "Roboto",sans-serif;color:var(--muted)}
.car-dots{top:1600px;left:560px;display:flex;gap:12px}
.car-dots span{width:11px;height:11px;border-radius:50%;border:1.5px solid var(--accent)}
.car-dots span.on{background:var(--accent)}

/* earn */
.panel{top:1928px;width:533px;height:393px;color:var(--white)}
.panel h3{position:absolute;top:88px;font:400 27px "Roboto",sans-serif}
.panel p{position:absolute;top:148px;width:300px;font:400 13.5px/22px "Roboto",sans-serif}
.btn-ghost{position:absolute;height:37px;border:1.5px solid var(--white);border-radius:19px;font:400 13.5px/34px "Roboto",sans-serif;text-align:center;color:var(--white)}

/* testimonials */
.avatar{left:564px;top:2552px;width:72px;height:72px;border-radius:50%;background:radial-gradient(circle at 50% 40%,#c9a08b 0%,#7b5a4c 60%,#3f3733 100%)}
.quote{left:200px;top:2674px;width:800px;text-align:center;font:400 13.5px/20px "Roboto",sans-serif;color:var(--muted)}

/* cta */
.cta{left:0;top:2877px;width:1200px;height:400px;background:linear-gradient(120deg,#3a3633 0%,#1f1d1c 40%,#2c2b2a 70%,#4a4744 100%)}
.cta-title{top:2949px;font:400 27px "Open Sans",sans-serif;letter-spacing:1.5px;color:var(--white)}
.btn-solid{left:537px;top:3030px;width:124px;height:36px;border-radius:18px;background:var(--accent);color:var(--white);font:400 14px/36px "Roboto",sans-serif;text-align:center}
.cta-line{font:400 11.5px "Roboto",sans-serif;color:var(--white)}
.cta-line.small{font-size:10.5px}

/* footer */
.footer{left:0;top:3277px;width:1200px;height:68px;background:var(--footer)}
.footer-links{left:189px;top:3291px;font:400 9.5px "Roboto",sans-serif;color:var(--white)}
.social{left:929px;top:3290px;display:flex;gap:9px}
.social span{width:14px;height:14px;border-radius:50%;background:var(--white)}
.copyright{top:3321px;font:400 9.5px "Roboto",sans-serif;color:var(--white)}
</style>
</head>
<body>

<header>
  <div class="abs hero" role="img" aria-label="Photo of a dark grey sports coupe parked on a roadside under a cloudy sky"></div>
  <div class="abs hero-car" aria-hidden="true"></div>
  <div class="abs brand">Wheelora</div>
  <nav class="abs nav">
    <a style="left:7px">About us</a>
    <a style="left:100px">Help</a>
    <a style="left:171px">Contact</a>
    <a style="left:256px">Support</a>
    <a style="left:344px">Sign Up</a>
  </nav>
  <div class="abs pill login">Login</div>
  <div class="abs pill rent">Rent your car</div>

  <h1 class="abs center hero-title">Cars around you,<br>ready to go</h1>
  <p class="abs center hero-sub">For a few hours or a few days</p>

  <form class="abs search">
    <div class="field" style="width:182px">
      <div class="label">Pick Up</div><div class="value">Choose Location</div>
      <svg class="chev" width="8" height="5" viewBox="0 0 8 5"><path d="M1 1l3 3 3-3" fill="none" stroke="#999" stroke-width="1"/></svg>
    </div>
    <div class="field" style="width:147px">
      <div class="label">Start Date</div><div class="value">Choose Date</div>
      <svg class="chev" width="8" height="5" viewBox="0 0 8 5"><path d="M1 1l3 3 3-3" fill="none" stroke="#999" stroke-width="1"/></svg>
    </div>
    <div class="field" style="width:147px">
      <div class="label">Return Date</div><div class="value">Choose Date</div>
      <svg class="chev" width="8" height="5" viewBox="0 0 8 5"><path d="M1 1l3 3 3-3" fill="none" stroke="#999" stroke-width="1"/></svg>
    </div>
    <div class="go">GO
      <svg width="16" height="13" viewBox="0 0 16 13"><path d="M1.5 7l4.5 4.5L14.5 1.5" fill="none" stroke="var(--accent)" stroke-width="2.5"/></svg>
    </div>
  </form>
  <div class="abs hero-dots"><span></span><span class="on"></span><span></span></div>
</header>

<section>
  <h2 class="abs center section-title" style="top:633px">Discover cars for rent</h2>
  <div class="abs rule" style="top:677px"></div>
  <p class="abs body-text intro">Lorem ipsum dolor sit amet, consectetur adipiscing elit, sed do eiusmod tempor incididunt ut labore et dolore magna aliqua. Ut enim ad minim veniam, quis nostrud exercitation ullamco laboris nisi ut aliquip ex ea commodo consequat. Duis aute irure dolor in reprehenderit in voluptate velit esse cillum dolore eu fugiat nulla pariatur.</p>

  <div class="abs feature" style="left:142px">
    <svg width="50" height="50" viewBox="0 0 50 50" fill="none" stroke="var(--accent)" stroke-width="3">
      <path d="M2 10h46M2 25h46M2 40h46"/>
      <circle cx="16" cy="10" r="4.5" fill="#fff"/><circle cx="33" cy="25" r="4.5" fill="#fff"/><circle cx="16" cy="40" r="4.5" fill="#fff"/>
    </svg>
    <h3>Flexibility</h3>
    <p>Lorem ipsum dolor sit amet, consectetur adipiscing elit, sed do eiusmod tempor incididunt ut labore et dolore</p>
  </div>
  <div class="abs feature" style="left:383px">
    <svg width="50" height="50" viewBox="0 0 50 50">
      <circle cx="25" cy="17" r="11" fill="var(--accent)"/>
      <path d="M11 17a14 14 0 0 1 28 0" fill="none" stroke="var(--accent)" stroke-width="3"/>
      <rect x="8" y="14" width="5" height="9" rx="2" fill="var(--accent)"/><rect x="37" y="14" width="5" height="9" rx="2" fill="var(--accent)"/>
      <path d="M6 50c0-12 8-18 19-18s19 6 19 18z" fill="var(--accent)"/>
    </svg>
    <h3>Service</h3>
    <p>Lorem ipsum dolor sit amet, consectetur adipiscing elit, sed do eiusmod tempor incididunt ut labore et dolore</p>
  </div>
  <div class="abs feature" style="left:618px">
    <svg width="50" height="54" viewBox="0 0 50 54">
      <path d="M25 2l21 8v16c0 13-9 22-21 26C13 48 4 39 4 26V10z" fill="var(--accent)"/>
      <path d="M15 27l7 7 13-14" fill="none" stroke="#fff" stroke-width="4.5"/>
    </svg>
    <h3>Security</h3>
    <p>Lorem ipsum dolor sit amet, consectetur adipiscing elit, sed do eiusmod tempor incididunt ut labore et dolore</p>
  </div>
  <div class="abs feature" style="left:852px">
    <svg width="64" height="64" viewBox="0 0 64 64" fill="none" stroke="var(--accent)" stroke-width="2.2">
      <rect x="21" y="6" width="22" height="50" rx="4" transform="rotate(15 32 31)"/>
      <circle cx="26" cy="51" r="1.5" fill="var(--accent)"/>
      <path d="M12 20c-4 6-4 14 0 20M7 16c-6 9-6 21 0 30M52 22c4 6 4 14 0 20M57 18c6 9 6 21 0 30"/>
    </svg>
    <h3>Freedom</h3>
    <p>Lorem ipsum dolor sit amet, consectetur adipiscing elit, sed do eiusmod tempor incididunt ut labore et dolore</p>
  </div>
</section>

<section>
  <div class="abs featured"></div>
  <h2 class="abs center section-title" style="top:1250px">Featured Cars</h2>
  <div class="abs rule" style="top:1293px"></div>

  <article class="abs card" style="left:156px">
    <div class="photo" role="img" aria-label="White electric sedan parked on grass in front of trees" style="background:linear-gradient(180deg,#b9cfe4 0%,#4d7a3d 45%,#5f8f3a 100%)"></div>
    <div class="info">
      <h4>Voltline E3</h4>
      <p class="desc">Lorem ipsum dolor sit amet, consectetur adipiscing elit, sed do eiusmod tempor incididunt ut labore et dolore magna aliqua. Ut enim ad minim veniam, quis</p>
      <div class="price">38 $ /day</div>
      <div class="stars">
        <svg width="78" height="11" viewBox="0 0 78 11" fill="var(--accent)"><g id="s"><path d="M5.5 0l1.6 3.6 3.9.4-2.9 2.6.8 3.9-3.4-2-3.4 2 .8-3.9L0 4l3.9-.4z"/></g><use href="#s" x="16"/><use href="#s" x="32"/><use href="#s" x="48"/><use href="#s" x="64"/></svg>
        <span>23</span>
      </div>
      <div class="divider"></div>
      <div class="loc"><svg width="8" height="11" viewBox="0 0 8 11"><path d="M4 0a4 4 0 0 1 4 4c0 3-4 7-4 7S0 7 0 4a4 4 0 0 1 4-4z" fill="#222"/><circle cx="4" cy="4" r="1.5" fill="#fff"/></svg>Location</div>
    </div>
  </article>

  <article class="abs card" style="left:540px">
    <div class="photo" role="img" aria-label="Front view of a dark grey saloon car at sunset" style="background:linear-gradient(180deg,#c99a4a 0%,#5b5347 35%,#3d4146 70%,#6b6b6b 100%)"></div>
    <div class="info">
      <h4>Bavaro</h4>
      <p class="desc">Lorem ipsum dolor sit amet, consectetur adipiscing elit, sed do eiusmod tempor incididunt ut labore et dolore magna aliqua. Ut enim ad minim veniam, quis</p>
      <div class="price">38 $ /day</div>
      <div class="stars">
        <svg width="78" height="11" viewBox="0 0 78 11" fill="var(--accent)"><use href="#s"/><use href="#s" x="16"/><use href="#s" x="32"/><use href="#s" x="48"/><use href="#s" x="64"/></svg>
        <span>23</span>
      </div>
      <div class="divider"></div>
      <div class="loc"><svg width="8" height="11" viewBox="0 0 8 11"><path d="M4 0a4 4 0 0 1 4 4c0 3-4 7-4 7S0 7 0 4a4 4 0 0 1 4-4z" fill="#222"/><circle cx="4" cy="4" r="1.5" fill="#fff"/></svg>Location</div>
    </div>
  </article>

  <article class="abs card" style="left:925px">
    <div class="photo" role="img" aria-label="Rear view of a dark grey sports coupe on a road" style="background:linear-gradient(180deg,#9aa1a8 0%,#505457 45%,#2f3133 70%,#7b7670 100%)"></div>
    <div class="info">
      <h4>Stallion GT</h4>
      <p class="desc">Lorem ipsum dolor sit amet, consectetur adipiscing elit, sed do eiusmod tempor incididunt ut labore et dolore magna aliqua. Ut enim ad minim veniam, quis</p>
      <div class="price">38 $ /day</div>
      <div class="stars">
        <svg width="78" height="11" viewBox="0 0 78 11" fill="var(--accent)"><use href="#s"/><use href="#s" x="16"/><use href="#s" x="32"/><use href="#s" x="48"/><use href="#s" x="64"/></svg>
        <span>23</span>
      </div>
      <div class="divider"></div>
      <div class="loc"><svg width="8" height="11" viewBox="0 0 8 11"><path d="M4 0a4 4 0 0 1 4 4c0 3-4 7-4 7S0 7 0 4a4 4 0 0 1 4-4z" fill="#222"/><circle cx="4" cy="4" r="1.5" fill="#fff"/></svg>Location</div>
    </div>
  </article>

  <div class="abs car-dots"><span class="on"></span><span></span><span></span><span></span></div>
</section>

<section>
  <h2 class="abs center section-title" style="top:1800px">Make Money With Your Car</h2>
  <div class="abs rule" style="top:1844px"></div>

  <div class="abs panel" style="left:44px;background:linear-gradient(135deg,#7d8584 0%,#4d5051 45%,#5d5b58 75%,#3e3f40 100%)" role="img" aria-label="Two people shaking hands over a desk with papers and a laptop">
    <h3 style="left:85px">RENT YOUR CAR</h3>
    <p style="left:85px">Decide when you want to rent out your vehicle and to whom. Manage your requests on our website, choose your drivers and earn money with each rental.</p>
    <div class="btn-ghost" style="left:85px;top:292px;width:125px">Learn more</div>
  </div>

  <div class="abs panel" style="left:620px;background:linear-gradient(135deg,#6a6257 0%,#4a4642 40%,#59544c 70%,#3f3c39 100%)" role="img" aria-label="Aerial view of a car park entrance with barrier booths">
    <h3 style="left:79px">PARK AND EARN</h3>
    <p style="left:79px;width:290px">Let your car work for you. We'll keep it in our cark park and manage your bookings. You don't need to do a thing. Just earn money!</p>
    <div class="btn-ghost" style="left:79px;top:283px;width:125px">Learn more</div>
  </div>
</section>

<section>
  <h2 class="abs center section-title" style="top:2410px">Testimonials</h2>
  <p class="abs center" style="top:2464px;font:400 11.5px 'Roboto',sans-serif;color:var(--muted)">Here's what others are saying about us</p>
  <svg class="abs" style="left:92px;top:2578px" width="14" height="22" viewBox="0 0 14 22"><path d="M12 1L2 11l10 10" fill="none" stroke="#555" stroke-width="1.6"/></svg>
  <svg class="abs" style="left:1094px;top:2578px" width="14" height="22" viewBox="0 0 14 22"><path d="M2 1l10 10L2 21" fill="none" stroke="#555" stroke-width="1.6"/></svg>
  <div class="abs avatar" role="img" aria-label="Portrait photo of a customer"></div>
  <p class="abs center" style="top:2645px;font:400 11.5px 'Roboto',sans-serif;color:var(--muted)">Name and Car Details</p>
  <p class="abs quote">Lorem ipsum dolor sit amet, consectetur adipiscing elit, sed do eiusmod tempor incididunt ut labore et dolore magna aliqua. Ut enim ad minim veniam, quis nostr</p>
</section>

<section>
  <div class="abs cta" role="img" aria-label="Dark blurred night photo with warm bokeh lights"></div>
  <h2 class="abs center cta-title">Looking to rent a car?</h2>
  <div class="abs rule" style="top:2993px;width:70px;left:565px"></div>
  <div class="abs btn-solid">Rent Now</div>
  <p class="abs center cta-line small" style="top:3107px">Issues while booking?</p>
  <p class="abs center cta-line" style="top:3130px">Check FAQs</p>
  <p class="abs center cta-line small" style="top:3155px">or</p>
  <p class="abs center cta-line" style="top:3179px">Contact Us</p>
</section>

<footer>
  <div class="abs footer"></div>
  <p class="abs footer-links">Privacy Policy | Customs Info | Legal Notice | Cancellation Policy</p>
  <div class="abs social"><span></span><span></span><span></span><span></span><span></span></div>
  <p class="abs center copyright">©Wheelora 2018 &nbsp;| All Rights Reserved reserved |</p>
</footer>

</body>
</html>
```